Brochure Design Project

We are a payroll company. We offer a wide variety of products and services:
1. Payroll Processing
2. Employee Direct Deposit
3. Time and attendance
4. HR services
5. Employee Employee Benefits

I'd like to develop a one page template that uses a combination of our logo (attached), colors (attached) and possible a picture. The picture could be shown as an option as it may change based on the product or service.

Target Market(s)

Adults in the United States ages 22-50. Typically these people are accountants, human resource professionals or entrepreneurs. The payroll industry is dominated by 3 large payroll processors, QLM, Wendrafy and Tolvarex. These companies are very impersonal and make it difficult to resolve issues when they arise. We have grown to over 400 clients by being the opposite of the big guys,

Industry/Entity Type

It Company

Font styles to use
Sans Serif

Requirements
Must have
• The brochure can be one or two pages.
Nice to have
• I'll know it when I see it but I can't describe it. I have attached a few brochures that have caught my eye.
Should not have
• No cartoons. No money signs. Hip, new, fresh are words I'd use to describe the winning product. Of the three people I described in my target market, the entrepreneur is the market I'd most like to target.

```html
<!DOCTYPE html>
<html lang="en">
<head>
<meta charset="utf-8">
<title>Ledgerly Payroll – Services Brochure</title>
<link rel="stylesheet" href="https://fonts.googleapis.com/css2?family=Montserrat:wght@500;600;800&display=swap">
<style>
  :root {
    --brand-blue: #161c8f;
    --brand-green: #9bf531;
    --brand-ink: #111111;
    --brand-white: #ffffff;
    --stone-light: #a3a6a8;
    --stone-dark: #5f6365;
    --bullet-light: #ff7a66;
    --bullet-dark: #b30000;
  }
  html, body {
    margin: 0;
    padding: 0;
    overflow: hidden;
    background: var(--brand-white);
  }
  .brochure {
    position: relative;
    width: 950px;
    height: 1200px;
    overflow: hidden;
    background: var(--brand-white);
    font-family: "Montserrat", Arial, sans-serif;
  }
  .brochure__bands {
    position: absolute;
    inset: 0;
  }
  .brand {
    position: absolute;
    left: 62px;
    top: 24px;
    margin: 0;
    color: var(--brand-blue);
    font-weight: 800;
    font-size: 54px;
    line-height: 0.98;
    letter-spacing: 1px;
  }
  .brand span {
    display: block;
    padding-left: 18px;
    font-size: 38px;
    letter-spacing: 5px;
  }
  .tagline {
    position: absolute;
    left: 88px;
    top: 448px;
    margin: 0;
    transform-origin: 0 100%;
    transform: rotate(-34.5deg);
    color: var(--brand-ink);
    font-weight: 600;
    font-size: 29px;
    white-space: nowrap;
    line-height: 1;
  }
  .services {
    list-style: none;
    margin: 0;
    padding: 0;
  }
  .service {
    position: absolute;
    color: var(--brand-white);
    font-weight: 500;
    font-size: 32px;
    line-height: 39px;
    letter-spacing: 0.5px;
    padding-left: 24px;
  }
  .service::before {
    content: "";
    position: absolute;
    left: 0;
    top: 11px;
    width: 17px;
    height: 17px;
    border-radius: 50%;
    background: radial-gradient(circle at 35% 30%, var(--bullet-light), var(--bullet-dark) 70%);
  }
  .service--hr { left: 700px; top: 68px; }
  .service--deposit { left: 531px; top: 189px; }
  .service--time { left: 348px; top: 325px; }
  .service--processing { left: 191px; top: 437px; }
  .service--benefits { left: 47px; top: 547px; }
</style>
</head>
<body>
<main class="brochure">
  <svg class="brochure__bands" width="950" height="1200" viewBox="0 0 950 1200" aria-hidden="true">
    <defs>
      <linearGradient id="stoneGradient" x1="0" y1="0" x2="0" y2="1">
        <stop offset="0" stop-color="#a3a6a8"/>
        <stop offset="1" stop-color="#5f6365"/>
      </linearGradient>
      <linearGradient id="documentGradient" x1="0" y1="0" x2="1" y2="1">
        <stop offset="0" stop-color="#e2e2e2"/>
        <stop offset="1" stop-color="#b4b5b6"/>
      </linearGradient>
    </defs>
    <polygon class="band band--blue" points="0,545 790,0 950,0 950,255 0,940" fill="#161c8f"/>
    <polygon class="band band--rule" points="0,940 950,255 950,287 0,976" fill="#111111"/>
    <polygon class="band band--green" points="0,976 950,287 950,572 93,1200 0,1200" fill="#9bf531"/>
    <polygon class="band band--rule" points="93,1200 950,572 950,590 117,1200" fill="#111111"/>
    <polygon class="band band--stone" points="117,1200 950,590 950,1200" fill="url(#stoneGradient)"/>
    <rect class="highlight-panel" x="525" y="597" width="415" height="261" fill="#ffffff" opacity="0.32"/>
    <rect class="highlight-panel" x="172" y="858" width="308" height="342" fill="#ffffff" opacity="0.32"/>
    <rect class="feature-photo" x="528" y="922" width="422" height="278" fill="url(#documentGradient)" role="img" aria-label="Photo of a certified payroll form with a red check mark"/>
  </svg>

  <h1 class="brand">Ledgerly<span>Payroll</span></h1>

  <p class="tagline">We become better as you come nearer…</p>

  <ul class="services">
    <li class="service service--hr">HR Services</li>
    <li class="service service--deposit">Employee Direct<br>Deposit</li>
    <li class="service service--time">Time and Attendance</li>
    <li class="service service--processing">Payroll Processing</li>
    <li class="service service--benefits">Employee Employee<br>Benefits</li>
  </ul>
</main>
</body>
</html>
```